Tolvex Engineers: Why you should hire us keepsake

New design. Open to plastic cards. We are an engineering firm that designs cell phone towers and commercial buildings. Please check out our website www.tolvexgrp.com for more details. We want people to remember our card and for it to be useful if possible. We want the same look and feel on these cards to be translated to other marketing material we may need such as brochures.

Target Market(s)

Architects, Developers and Telecommunication Carriers

Industry/Entity Type

Engineering

Contact Information for Business Card

Card with our company colors, logo, and innovative design with elements related to our industry.

Font styles to use
Sans Serif

Colors
9bcb3c
abd036
0255a3

Requirements
Must have
• Sleek and hip design
Nice to have
• Bright lime green and navy coloring that pops with an innovative design.
Should not have
• A basic and boring design

```html
<!DOCTYPE html>
<html lang="en">
<head>
<meta charset="utf-8">
<title>Tolvex Engineers – Business Card</title>
<link href="https://fonts.googleapis.com/css2?family=Arimo:wght@400;700&display=swap" rel="stylesheet">
<style>
  :root {
    --page-bg: #d9d6d1;
    --navy-deep: #0c1f4a;
    --navy-mid: #14306a;
    --lime: #22b21e;
    --lime-bright: #2fc42a;
    --frost: #e6e6e4;
    --frost-edge: #d3d4d3;
    --text-light: #d8dce6;
    --name-light: #e2e0da;
    --ink: #1f2d4a;
  }
  * { margin: 0; padding: 0; box-sizing: border-box; }
  html, body {
    width: 1200px; height: 970px; overflow: hidden;
    background: var(--page-bg);
    font-family: "Arimo", Arial, sans-serif;
  }
  .card {
    position: absolute; left: 100px; top: 207px;
    width: 1000px; height: 556px;
    display: flex;
    box-shadow: 0 18px 40px rgba(0,0,0,.22);
  }
  .card-front {
    position: relative; width: 516px; height: 100%;
    background: linear-gradient(160deg, var(--navy-mid) 0%, var(--navy-deep) 55%, #1a2d55 100%);
    color: var(--text-light);
  }
  .divider {
    position: relative; width: 10px; height: 100%;
    background: var(--lime);
  }
  .divider-notch {
    position: absolute; left: -24px; top: 96px;
  }
  .card-brand {
    position: relative; flex: 1; height: 100%;
    background: linear-gradient(180deg, var(--frost) 0%, var(--frost-edge) 100%);
  }
  .holder-name {
    position: absolute; right: 77px; top: 117px;
    font-weight: 700; font-size: 29px; letter-spacing: .5px;
    color: var(--name-light); white-space: nowrap;
  }
  .details {
    position: absolute; right: 77px; top: 290px;
    text-align: right; font-size: 21px; line-height: 29px;
  }
  .discipline { color: var(--lime-bright); font-size: 21px; }
  .contact {
    position: absolute; right: 77px; top: 412px;
    text-align: right; font-size: 21px;
  }
  .contact-row {
    display: flex; justify-content: flex-end; align-items: center;
    gap: 12px; height: 30px;
  }
  .contact-row svg { width: 22px; height: 22px; }
  .brand-name {
    position: absolute; left: 0; right: 0; top: 120px;
    text-align: center; font-weight: 700; font-size: 52px;
    color: var(--lime-bright); line-height: 1.1;
  }
  .brand-web {
    position: absolute; left: 0; right: 0; top: 473px;
    text-align: center; font-size: 21px; letter-spacing: 8px;
    color: var(--ink);
  }
</style>
</head>
<body>
  <div class="card">
    <section class="card-front">
      <h1 class="holder-name">DANA WHITLOCK REYES</h1>
      <div class="details">
        <p class="discipline">MULTI-DISCIPLINE ENGINEERING</p>
        <p>2400 Cedar Ridge Pkwy</p>
        <p>Suite 310 Alder, GA 30190</p>
      </div>
      <div class="contact">
        <div class="contact-row"><span>706.555.0142</span>
          <svg viewBox="0 0 22 22"><rect x="5" y="1" width="12" height="20" rx="2" fill="none" stroke="#2fc42a" stroke-width="2.4"/><rect x="8" y="4" width="6" height="11" fill="#2fc42a"/></svg>
        </div>
        <div class="contact-row"><span>678.555.0198</span>
          <svg viewBox="0 0 22 22"><path d="M5 2 L9 2 L10 7 L7.5 9 C9 12.5 10.5 14 13.5 15.5 L15.5 13 L20 14 L20 18 C20 19 19 20 18 20 C9 19.5 3 13 2.5 4.5 C2.5 3 3.5 2 5 2 Z" fill="#2fc42a"/></svg>
        </div>
        <div class="contact-row"><span>dreyes@tolvexgrp.com</span>
          <svg viewBox="0 0 22 22"><rect x="1" y="4" width="20" height="14" fill="#2fc42a"/><path d="M1 4 L11 12 L21 4 M1 18 L8 10 M21 18 L14 10" fill="none" stroke="#0c1f4a" stroke-width="1.6"/></svg>
        </div>
      </div>
    </section>
    <div class="divider">
      <svg class="divider-notch" width="26" height="80" viewBox="0 0 26 80"><polygon points="26,0 26,80 0,40" fill="#22b21e"/></svg>
    </div>
    <section class="card-brand">
      <p class="brand-name">Tolvex<br>Engineers</p>
      <p class="brand-web">www.tolvexgrp.com</p>
    </section>
  </div>
</body>
</html>
```